Aged Care Consultancy Business needs a business card design

I need a two sided business card - I want it clean and professional. Surprise me

Target Market(s)

middle aged and ageing victorians

Industry/Entity Type

Health Care

Contact Information for Business Card

Text to be included

Logo
Aged Care Consulting Services
Professional, Reliable, Affordable

Orin Tessaldo
Director
0472 31 64 09 (larger)
1300 31 64 09
orin@valtrino.com.au
www.valtrinocare.com.au
Facebook (details TBA)

include little icons beside the contact info:

- Envelope = email
- Phone = phone
- Globe = website

Font styles to use
Serif
Sans Serif

Requirements
Must have
• look proffesional and clean

```html
<!DOCTYPE html>
<html lang="en">
<head>
<meta charset="utf-8">
<title>Valtrino Care – Business Card</title>
<link rel="stylesheet" href="https://fonts.googleapis.com/css2?family=Open+Sans:wght@400;600;700&display=swap">
<style>
  :root {
    --navy: #1d4585;
    --navy-deep: #0c1f4d;
    --navy-mid: #173a78;
    --orange: #e8901f;
    --paper: #ffffff;
    --backdrop: #e9eaec;
    --frame: #5a78aa;
  }
  * { box-sizing: border-box; margin: 0; padding: 0; }
  html, body { width: 1200px; height: 1200px; overflow: hidden; }
  body {
    background: var(--backdrop);
    font-family: "Open Sans", Arial, sans-serif;
    position: relative;
  }
  .card {
    position: absolute;
    left: 150px;
    width: 900px;
    height: 514px;
    border-radius: 4px;
    box-shadow: 0 10px 30px rgba(0,0,0,0.18);
    overflow: hidden;
  }
  .card--front { top: 70px; background: var(--paper); }
  .card--back {
    top: 616px;
    background: radial-gradient(ellipse at 50% 50%, var(--navy-mid) 0%, var(--navy-deep) 80%);
  }

  .front-frame {
    position: absolute;
    left: 70px; top: 56px;
    width: 510px; height: 300px;
    border-top: 1.5px solid var(--frame);
    border-left: 1.5px solid var(--frame);
  }
  .holder {
    position: absolute;
    left: 596px; top: 36px;
  }
  .holder__name {
    display: flex; align-items: center; gap: 10px;
    color: var(--orange);
    font-weight: 700;
    font-size: 28px;
    letter-spacing: 0.5px;
    text-transform: uppercase;
  }
  .holder__role {
    color: var(--navy);
    font-size: 17px;
    margin: 2px 0 0 36px;
  }

  .wordmark {
    display: flex; align-items: center;
    font-weight: 700;
    letter-spacing: 0.5px;
  }
  .wordmark__dot { border-radius: 50%; flex: none; }

  .brand-block {
    position: absolute;
    left: 150px; top: 140px;
  }
  .brand-block .wordmark { gap: 18px; font-size: 58px; color: var(--navy); line-height: 1.1; }
  .brand-block .wordmark__dot { width: 58px; height: 58px; background: var(--orange); }
  .tagline {
    margin: 10px 0 0 76px;
    color: var(--navy);
    font-size: 17px;
    font-weight: 600;
    line-height: 1.35;
  }
  .tagline__values { color: var(--orange); font-weight: 400; font-size: 15px; }

  .card--back .wordmark {
    position: absolute;
    left: 0; right: 0; top: 0; bottom: 0;
    justify-content: center; gap: 28px;
    font-size: 96px; color: var(--paper);
  }
  .card--back .wordmark__dot { width: 96px; height: 96px; background: var(--paper); }

  .contacts {
    position: absolute;
    left: 78px; top: 366px;
    list-style: none;
    color: var(--navy);
    font-size: 17px;
    line-height: 1.3;
  }
  .contacts li { display: flex; align-items: center; gap: 8px; }
  .contacts .contact--primary { font-size: 20px; }
  .icon { width: 17px; height: 17px; flex: none; }
</style>
</head>
<body>

<section class="card card--front" aria-label="Business card front">
  <div class="front-frame"></div>

  <div class="holder">
    <p class="holder__name">
      <svg class="icon" viewBox="0 0 20 20" aria-hidden="true" style="width:26px;height:26px">
        <circle cx="10" cy="6" r="4.5" fill="var(--navy)"/>
        <path d="M1 20 C1 12 19 12 19 20 Z" fill="var(--navy)"/>
      </svg>
      Orin Tessaldo
    </p>
    <p class="holder__role">Director</p>
  </div>

  <div class="brand-block">
    <div class="wordmark">
      <span class="wordmark__dot"></span>
      <span>valtrino care</span>
    </div>
    <p class="tagline">Aged Care Consulting Services<br>
      <span class="tagline__values">Professional, Reliable, Affordable</span></p>
  </div>

  <ul class="contacts">
    <li class="contact--primary">
      <svg class="icon" viewBox="0 0 18 18" aria-hidden="true"><rect width="18" height="18" rx="3" fill="var(--navy)"/><rect x="5.5" y="3" width="7" height="12" rx="1.2" fill="#fff"/><rect x="7" y="4.5" width="4" height="7" fill="var(--navy)"/></svg>
      0472 31 64 09
    </li>
    <li>
      <svg class="icon" viewBox="0 0 18 18" aria-hidden="true"><rect width="18" height="18" rx="3" fill="var(--navy)"/></svg>
      Social page link
    </li>
    <li>
      <svg class="icon" viewBox="0 0 18 18" aria-hidden="true"><rect width="18" height="18" rx="3" fill="var(--navy)"/><rect x="3.5" y="5" width="11" height="8" fill="#fff"/><path d="M3.5 5 L9 9.5 L14.5 5" stroke="var(--navy)" stroke-width="1.2" fill="none"/></svg>
      orin@valtrino.com.au
    </li>
    <li>
      <svg class="icon" viewBox="0 0 18 18" aria-hidden="true"><rect width="18" height="18" rx="3" fill="var(--navy)"/><path d="M5 4 L7.5 4 L8.5 7 L7 8 C7.8 9.8 8.8 10.8 10.5 11.5 L11.5 10 L14 11 L14 13.5 C9 14 4.5 9.5 5 4 Z" fill="#fff"/></svg>
      1300 31 64 09
    </li>
    <li>
      <svg class="icon" viewBox="0 0 18 18" aria-hidden="true"><rect width="18" height="18" rx="3" fill="var(--navy)"/><circle cx="9" cy="9" r="5.5" fill="none" stroke="#fff" stroke-width="1.2"/><ellipse cx="9" cy="9" rx="2.3" ry="5.5" fill="none" stroke="#fff" stroke-width="1"/><line x1="3.5" y1="9" x2="14.5" y2="9" stroke="#fff" stroke-width="1"/></svg>
      www.valtrinocare.com.au
    </li>
  </ul>
</section>

<section class="card card--back" aria-label="Business card back">
  <div class="wordmark">
    <span class="wordmark__dot"></span>
    <span>valtrino care</span>
  </div>
</section>

</body>
</html>
```